Business Card Design for ReaL ESTATE AGENT

New Business Cards for a real estate agent in Jacksonville, FL. My specialty is urban core, historic districts but sell through out the city. Company Name is Quill and Harbor Realty a division of the Vantrell Companies. The card needs to convey an essence of professionalism, knowledge and success.

Target Market(s)

Home buyers and Sellers

Industry/Entity Type

Real Estate

Contact Information for Business Card

Double sided

Font styles to use
Sans Serif

Requirements
Must have
• My logs and photo (provided). My contact information as follows:
• Derek Holloway
• Cell 904-618-3092
• Office 904-731-6248
• Email derekholloway@mailvantor.com
Nice to have
• Tag Line - Exceptional Effort. Proven Results.

```html
<!DOCTYPE html>
<html lang="en">
<head>
<meta charset="UTF-8">
<title>Quill and Harbor Realty – Business Card</title>
<link href="https://fonts.googleapis.com/css2?family=Open+Sans:wght@400;600&display=swap" rel="stylesheet">
<style>
  :root {
    --page-bg: #2a2a2c;
    --card-bg: #1b1b1d;
    --card-edge: #262628;
    --accent-red: #e4503a;
    --brand-green: #1f5b3a;
    --text-light: #e9e9e9;
    --text-muted: #b9b9b9;
    --photo-dark: #233038;
    --photo-mid: #4a5b63;
  }
  * { box-sizing: border-box; margin: 0; padding: 0; }
  html, body {
    width: 1200px;
    height: 900px;
    overflow: hidden;
    background: var(--page-bg);
    font-family: "Open Sans", Arial, sans-serif;
  }
  .canvas {
    position: relative;
    width: 1200px;
    height: 900px;
  }
  .card {
    position: absolute;
    top: 300px;
    width: 525px;
    height: 300px;
    background: var(--card-bg);
    border: 1px solid var(--card-edge);
    border-radius: 22px;
  }
  .card--front { left: 50px; }
  .card--back  { left: 625px; }

  .portrait {
    position: absolute;
    left: 34px;
    top: 58px;
    width: 196px;
    height: 184px;
    border-radius: 14px;
    background: radial-gradient(circle at 40% 35%, var(--photo-mid), var(--photo-dark) 75%);
  }
  .details {
    position: absolute;
    left: 256px;
    top: 64px;
    color: var(--text-light);
  }
  .details__name {
    font-size: 25px;
    font-weight: 400;
    color: var(--accent-red);
    line-height: 1.1;
  }
  .details__title {
    font-size: 14px;
    margin-top: 4px;
  }
  .contact-list {
    list-style: none;
    margin-top: 20px;
  }
  .contact-list__item {
    display: flex;
    align-items: center;
    gap: 10px;
    font-size: 14px;
    margin-bottom: 8px;
    white-space: nowrap;
  }
  .contact-list__label {
    color: var(--text-muted);
    width: 46px;
  }
  .contact-list__icon {
    flex: none;
    width: 18px;
    height: 18px;
    border-radius: 3px;
    background: var(--accent-red);
    display: flex;
    align-items: center;
    justify-content: center;
  }

  .brand {
    position: absolute;
    inset: 0;
    display: flex;
    flex-direction: column;
    align-items: center;
    justify-content: center;
    gap: 14px;
  }
  .brand__mark {
    width: 76px;
    height: 76px;
    border-radius: 50%;
    background: var(--brand-green);
  }
  .brand__name {
    font-size: 30px;
    font-weight: 600;
    color: var(--accent-red);
    letter-spacing: 0.5px;
  }
  .brand__tagline {
    font-size: 14px;
    color: var(--text-light);
    letter-spacing: 0.5px;
  }
</style>
</head>
<body>
  <main class="canvas">
    <section class="card card--front">
      <div class="portrait" role="img" aria-label="Portrait photo of the agent"></div>
      <div class="details">
        <h1 class="details__name">Derek Holloway</h1>
        <p class="details__title">Managing Director</p>
        <ul class="contact-list">
          <li class="contact-list__item">
            <span class="contact-list__icon">
              <svg width="12" height="12" viewBox="0 0 12 12" aria-hidden="true">
                <path d="M2.5 1.5 L4.5 1.5 L5.2 3.8 L4 4.8 C4.6 6.2 5.8 7.4 7.2 8 L8.2 6.8 L10.5 7.5 L10.5 9.5 C10.5 10 10 10.5 9.5 10.5 C5.4 10.5 1.5 6.6 1.5 2.5 C1.5 2 2 1.5 2.5 1.5 Z" fill="#fff"/>
              </svg>
            </span>
            <span class="contact-list__label">Cell</span>
            904-618-3092
          </li>
          <li class="contact-list__item">
            <span class="contact-list__icon">
              <svg width="12" height="12" viewBox="0 0 12 12" aria-hidden="true">
                <path d="M2.5 1.5 L4.5 1.5 L5.2 3.8 L4 4.8 C4.6 6.2 5.8 7.4 7.2 8 L8.2 6.8 L10.5 7.5 L10.5 9.5 C10.5 10 10 10.5 9.5 10.5 C5.4 10.5 1.5 6.6 1.5 2.5 C1.5 2 2 1.5 2.5 1.5 Z" fill="#fff"/>
              </svg>
            </span>
            <span class="contact-list__label">Office</span>
            904-731-6248
          </li>
          <li class="contact-list__item">
            <span class="contact-list__icon">
              <svg width="12" height="12" viewBox="0 0 12 12" aria-hidden="true">
                <rect x="1.5" y="3" width="9" height="6.5" rx="0.8" fill="none" stroke="#fff" stroke-width="1.2"/>
                <path d="M1.8 3.4 L6 6.6 L10.2 3.4" fill="none" stroke="#fff" stroke-width="1.2"/>
              </svg>
            </span>
            derekholloway@mailvantor.com
          </li>
        </ul>
      </div>
    </section>

    <section class="card card--back">
      <div class="brand">
        <span class="brand__mark"></span>
        <p class="brand__name">Quill and Harbor Realty</p>
        <p class="brand__tagline">Exceptional Effort. Proven Results.</p>
      </div>
    </section>
  </main>
</body>
</html>
```